GPS Tracker APP

Greetings,

We are looking for a UX designer to help us finalize the design of the qTrovel APP for iOS and Android. This is a GPS tracker app will be used by parents to track family cars or a small business with a fleet of vehicles. Its main benefits are family safety and fleet tracking.

We have created a pdf document (attached) with sample screens to show how the application should work. We also have a beta version available in the Quillan Market Pell Market that we will provide so you can download and use for your reference. The app design should be up to par with the usability and design of harbo88 app, Other examples are: plimsy app and kovrax gps app.

The designer must create and provide all the graphic assets so that our app developer can finalize the app.

```html
<!DOCTYPE html>
<html lang="en">
<head>
<meta charset="utf-8">
<title>qTrovel – GPS Tracker App Screens</title>
<link rel="stylesheet" href="https://fonts.googleapis.com/css2?family=Poppins:wght@400;500;600;700&display=swap">
<style>
:root{
  --blue:#0f6db8;
  --blue-dark:#0a4f8c;
  --navy:#0b2546;
  --ink:#1c2230;
  --muted:#6b7280;
  --line:#e3e6ea;
  --soft:#eef2f6;
  --green:#3aa845;
  --map:#dfe3e8;
  --map-green:#cfe6cf;
  --bg-top:#1580d1;
  --bg-bottom:#e5e2dd;
  --h-green:#5a8a2e;--h-blue:#1d9ad6;--h-gold:#b8911c;--h-red:#d8282c;--h-purple:#6a3c9c;
}
*{box-sizing:border-box}
html,body{margin:0;padding:0}
body{width:1200px;height:2774px;overflow:hidden;position:relative;
  background:linear-gradient(180deg,var(--bg-top) 0,#3f97d8 520px,var(--bg-bottom) 650px,var(--bg-bottom) 100%);
  font-family:'Poppins',sans-serif;color:var(--ink)}
.screen{position:absolute;width:220px;height:470px;background:#fff;border-radius:24px;overflow:hidden;font-size:8px;line-height:1.35}
.abs{position:absolute}
.map{background:var(--map)}
.bold{font-weight:700}
.up{text-transform:uppercase}
.blue{color:var(--blue)}
.muted{color:var(--muted)}
svg.i{width:14px;height:14px;fill:none;stroke:currentColor;stroke-width:2;stroke-linecap:round;stroke-linejoin:round}
.ico{width:32px;height:32px;border-radius:50%;background:var(--soft);color:var(--blue);display:flex;align-items:center;justify-content:center}
.ico.on{background:var(--blue);color:#fff}
.ico.lg{width:40px;height:40px}
.tabs{display:flex;justify-content:center;gap:16px;padding-top:14px}
.brand{font-weight:700;font-size:18px;letter-spacing:.5px;display:flex;align-items:center;gap:6px}
.brand .dot{width:18px;height:18px;border-radius:50%;background:currentColor}
.band{background:var(--blue);color:#fff;font-weight:700;font-size:8.5px;padding:5px 12px;text-transform:uppercase}
.head{display:flex;gap:8px;align-items:flex-start;padding:16px 10px 8px;font-weight:700;font-size:8px;text-transform:uppercase}
.back{width:18px;height:18px;border-radius:50%;background:var(--blue);color:#fff;display:flex;align-items:center;justify-content:center;flex:none}
.back.pale{background:var(--soft);color:var(--blue)}
.back svg{width:10px;height:10px}
.field .k{font-size:5.5px;color:var(--muted);text-transform:uppercase;font-weight:600}
.field .v{font-size:8px;font-weight:700;text-transform:uppercase;margin-bottom:7px}
.card{background:#fff;border-radius:8px;box-shadow:0 2px 8px rgba(0,0,0,.12)}
.status{display:flex;justify-content:space-around;padding:8px 10px;font-size:5px;text-align:center;color:var(--muted)}
.status .st{position:relative;color:var(--blue)}
.status .ok{position:absolute;top:-6px;right:-8px;width:10px;height:10px;border-radius:50%;background:var(--green)}
.row{display:flex;gap:9px;align-items:flex-start;padding:5px 14px}
.row .t{font-weight:700;font-size:8px;text-transform:uppercase}
.row .s{font-size:7px}
.stats{display:flex;justify-content:space-around;text-align:center;font-size:6px;color:var(--muted)}
.stats b{display:block;color:var(--ink);font-size:8px}
.stats .no b{color:var(--blue)}
.section{font-weight:700;font-size:8.5px;text-transform:uppercase;padding:8px 14px 2px}
.habits{display:flex;gap:6px;justify-content:center}
.habit{width:32px;height:32px;border-radius:50%;color:#fff;text-align:center;font-size:4px;font-weight:600;line-height:1;padding-top:6px;border:2px solid #fff;box-shadow:0 0 0 1px rgba(0,0,0,.08)}
.habit b{display:block;font-size:11px;margin-bottom:1px}
.chips{display:flex;justify-content:space-between;padding:14px 6px 0;font-size:5px;text-align:center;font-weight:600}
.chip{width:38px}
.chip .c{width:26px;height:26px;border-radius:50%;background:#111;margin:0 auto 3px}
.chip .c.b{background:var(--blue-dark)}
.chip .c.w{background:#fff;border:1px solid var(--line)}
.list-item{display:flex;align-items:center;gap:10px;padding:0 14px;height:30px;font-size:9px;font-weight:600;text-transform:uppercase}
.list-item .n{margin-left:auto;font-weight:600}
.list-item .blue-ico{color:var(--blue)}
</style>
</head>
<body>

<svg width="0" height="0" style="position:absolute" aria-hidden="true">
  <defs>
    <symbol id="car" viewBox="0 0 24 24"><path d="M5 16V11l2-5h10l2 5v5M4 16h16v3H4zM7 19v2M17 19v2M5 11h14"/><circle cx="8" cy="14" r=".5"/><circle cx="16" cy="14" r=".5"/></symbol>
    <symbol id="gear" viewBox="0 0 24 24"><circle cx="12" cy="12" r="3.5"/><path d="M12 2v3M12 19v3M2 12h3M19 12h3M4.9 4.9l2.1 2.1M17 17l2.1 2.1M4.9 19.1 7 17M17 7l2.1-2.1"/></symbol>
    <symbol id="chart" viewBox="0 0 24 24"><path d="M4 20h16M7 17v-5M11 17V8M15 17v-7M19 17V5"/></symbol>
    <symbol id="back" viewBox="0 0 24 24"><path d="M19 12H5M11 6l-6 6 6 6"/></symbol>
    <symbol id="chev" viewBox="0 0 24 24"><path d="M9 6l6 6-6 6"/></symbol>
    <symbol id="pin" viewBox="0 0 24 24"><path d="M12 21s-7-6.5-7-12a7 7 0 0 1 14 0c0 5.5-7 12-7 12z"/><circle cx="12" cy="9" r="2.5"/></symbol>
    <symbol id="home" viewBox="0 0 24 24"><path d="M3 11l9-7 9 7M6 10v10h12V10"/></symbol>
    <symbol id="user" viewBox="0 0 24 24"><circle cx="12" cy="8" r="4"/><path d="M4 21c1-5 15-5 16 0"/></symbol>
    <symbol id="bell" viewBox="0 0 24 24"><path d="M6 17V11a6 6 0 0 1 12 0v6l2 2H4zM10 21h4"/></symbol>
    <symbol id="gauge" viewBox="0 0 24 24"><path d="M4 16a8 8 0 1 1 16 0M12 16l4-5"/></symbol>
    <symbol id="bolt" viewBox="0 0 24 24"><path d="M13 3 5 14h6l-1 7 8-11h-6z"/></symbol>
    <symbol id="search" viewBox="0 0 24 24"><circle cx="11" cy="11" r="6"/><path d="M16 16l4 4"/></symbol>
    <symbol id="exit" viewBox="0 0 24 24"><path d="M10 4H5v16h5M14 8l4 4-4 4M8 12h10"/></symbol>
  </defs>
</svg>

<!-- ================= ROW 1 ================= -->

<!-- Login -->
<section class="screen login" style="left:61px;top:81px;background:var(--navy);color:#fff">
  <div class="abs" role="img" aria-label="Abstract blue data network background" style="inset:0 0 auto 0;height:250px;background:radial-gradient(circle at 70% 50%,#1f74c7 0,#0d3a6b 55%,var(--navy) 100%)"></div>
  <div class="abs brand" style="left:38px;top:32px;color:#fff"><span class="dot"></span>qTrovel</div>
  <div class="abs bold" style="left:0;right:0;top:165px;text-align:center;font-size:18px">LOGIN</div>
  <div class="abs" style="left:32px;right:32px;top:214px;font-size:9px;font-weight:600;border-bottom:1px solid rgba(255,255,255,.6);padding-bottom:4px">✉&nbsp; Email</div>
  <div class="abs" style="left:32px;right:32px;top:257px;font-size:9px;font-weight:600;border-bottom:1px solid rgba(255,255,255,.6);padding-bottom:4px">◉&nbsp; Password</div>
  <div class="abs" style="left:30px;right:34px;top:299px;height:26px;border-radius:13px;background:var(--blue);text-align:center;line-height:26px;font-size:9px;font-weight:600">Sign In</div>
  <div class="abs" style="left:0;right:0;top:350px;text-align:center;font-size:9px;font-weight:600">Forgot Your Password</div>
  <div class="abs" style="left:0;right:0;top:376px;text-align:center;font-size:9px;font-weight:600">Sign Up</div>
</section>

<!-- Map home -->
<section class="screen" style="left:351px;top:81px;background:#f1f3f6">
  <div class="abs map" role="img" aria-label="City street map with tracked vehicle zones" style="inset:0 0 90px 0"></div>
  <div class="abs" style="left:62px;top:120px;width:62px;height:62px;border-radius:50%;background:rgba(60,80,140,.55)"></div>
  <div class="abs" style="left:155px;top:108px;width:62px;height:62px;border-radius:50%;background:rgba(60,80,140,.55)"></div>
  <div class="abs" style="left:63px;top:240px;width:48px;height:48px;border-radius:50%;background:rgba(60,80,140,.55)"></div>
  <div class="abs" style="left:164px;top:240px;width:12px;height:12px;border-radius:50%;border:2px solid #e03a3a"></div>
  <div class="abs card" style="left:16px;right:16px;top:16px;height:24px;border-radius:12px;padding:0 10px;line-height:24px;font-size:8px;color:var(--muted)">Search
    <span class="abs ico on" style="right:4px;top:4px;width:16px;height:16px"><svg class="i" style="width:9px;height:9px"><use href="#search"/></svg></span></div>
  <div class="abs" style="left:0;right:0;bottom:0;height:90px;background:#fff;display:flex;justify-content:space-around;align-items:center;padding:0 18px">
    <span class="ico on lg"><svg class="i"><use href="#car"/></svg></span>
    <span class="ico lg"><svg class="i"><use href="#gear"/></svg></span>
    <span class="ico lg"><svg class="i"><use href="#chart"/></svg></span>
  </div>
</section>

<!-- Menu -->
<section class="screen" style="left:649px;top:81px">
  <div class="tabs" style="justify-content:flex-start;padding-left:18px"><span class="ico"><svg class="i"><use href="#car"/></svg></span><span class="ico on"><svg class="i"><use href="#gear"/></svg></span><span class="ico"><svg class="i"><use href="#chart"/></svg></span></div>
  <div class="brand" style="color:var(--navy);padding:18px 18px 14px;font-size:17px"><span class="dot" style="background:var(--blue)"></span>qTrovel</div>
  <div class="list-item" style="height:36px"><span class="ico" style="width:26px;height:26px"><svg class="i"><use href="#user"/></svg></span>Profile</div>
  <div class="list-item" style="height:36px"><span class="ico" style="width:26px;height:26px"><svg class="i"><use href="#car"/></svg></span>Subscription</div>
  <div class="list-item" style="height:36px"><span class="ico" style="width:26px;height:26px"><svg class="i"><use href="#chart"/></svg></span>Tutorials</div>
  <div class="list-item" style="height:36px"><span class="ico" style="width:26px;height:26px"><svg class="i"><use href="#bell"/></svg></span>Support</div>
  <div class="list-item blue" style="height:36px"><span class="ico" style="width:26px;height:26px"><svg class="i"><use href="#gear"/></svg></span>Alert Settings</div>
  <div class="list-item abs" style="bottom:14px;left:0"><span class="ico" style="width:26px;height:26px"><svg class="i"><use href="#exit"/></svg></span>Logout</div>
</section>

<!-- Alert settings -->
<section class="screen" style="left:922px;top:81px">
  <div class="tabs" style="justify-content:flex-start;padding-left:18px"><span class="ico"><svg class="i"><use href="#car"/></svg></span><span class="ico on"><svg class="i"><use href="#gear"/></svg></span><span class="ico"><svg class="i"><use href="#chart"/></svg></span></div>
  <div class="band" style="margin:14px 12px 10px 0;font-size:11px;padding:10px 20px">Alert Settings</div>
  <div class="list-item blue"><svg class="i"><use href="#pin"/></svg>Geo-Zones<svg class="i n" style="width:9px;color:var(--ink)"><use href="#chev"/></svg></div>
  <div class="list-item blue"><svg class="i"><use href="#bell"/></svg>Notifications<svg class="i n" style="width:9px;color:var(--ink)"><use href="#chev"/></svg></div>
  <div class="list-item blue"><svg class="i"><use href="#gauge"/></svg>Excessive Speed<svg class="i n" style="width:9px;color:var(--ink)"><use href="#chev"/></svg></div>
  <div class="list-item" style="font-size:7.5px"><svg class="i blue-ico"><use href="#car"/></svg>Hard Braking<svg class="i n" style="width:9px"><use href="#chev"/></svg></div>
  <div class="list-item" style="font-size:7.5px"><svg class="i blue-ico"><use href="#car"/></svg>Collison Detection<svg class="i n" style="width:9px"><use href="#chev"/></svg></div>
  <div class="list-item" style="font-size:7.5px"><svg class="i blue-ico"><use href="#gauge"/></svg>Rapid Acceleration<svg class="i n" style="width:9px"><use href="#chev"/></svg></div>
  <div class="list-item" style="font-size:7.5px"><svg class="i blue-ico"><use href="#car"/></svg>Curfew<svg class="i n" style="width:9px"><use href="#chev"/></svg></div>
  <div class="list-item blue"><svg class="i"><use href="#bolt"/></svg>Fuel Level<svg class="i n" style="width:9px;color:var(--ink)"><use href="#chev"/></svg></div>
</section>

<!-- ================= ROW 2 ================= -->

<!-- Devices -->
<section class="screen" style="left:61px;top:668px">
  <div class="abs map" role="img" aria-label="Street map with vehicle zones" style="inset:0 0 auto 0;height:205px"></div>
  <div class="abs" style="left:38px;top:122px;width:62px;height:62px;border-radius:50%;background:rgba(60,80,140,.55)"></div>
  <div class="abs" style="left:154px;top:110px;width:62px;height:62px;border-radius:50%;background:rgba(60,80,140,.55)"></div>
  <div class="abs card" style="left:14px;right:14px;top:16px;height:26px;border-radius:13px;padding:0 14px;line-height:26px;font-size:8px;color:var(--muted)">Search
    <span class="abs ico on" style="right:5px;top:5px;width:16px;height:16px"><svg class="i" style="width:9px;height:9px"><use href="#search"/></svg></span></div>
  <div class="abs" style="top:205px;left:0;right:0">
    <div class="tabs" style="padding-top:14px;gap:24px"><span class="ico on lg"><svg class="i"><use href="#car"/></svg></span><span class="ico lg"><svg class="i"><use href="#gear"/></svg></span><span class="ico lg"><svg class="i"><use href="#chart"/></svg></span></div>
    <div class="section" style="display:flex">Devices<span class="blue" style="margin-left:auto">+</span></div>
    <div class="card" style="margin:4px 12px 8px;padding:8px;display:flex;gap:8px;align-items:center;border-bottom:2px solid var(--green);font-size:6px;font-weight:600">
      <span style="width:28px;height:28px;border-radius:50%;background:var(--blue-dark);flex:none"></span>
      <span>VARRO V150 BLACK - HST-546<br>PARKED - AT SCHOOL<br>SINCE 2:06 PM</span></div>
    <div class="card" style="margin:0 12px 8px;padding:8px;display:flex;gap:8px;align-items:center;border-bottom:2px solid var(--green);font-size:6px;font-weight:600">
      <span style="width:28px;height:28px;border-radius:50%;background:#fff;border:1px solid var(--line);flex:none"></span>
      <span>CALDER WHITE -<br>FRL-389 PARKED - AT HOME<br>SINCE 2:06 PM</span></div>
    <div class="card" style="margin:0 12px;padding:8px;display:flex;gap:8px;align-items:center;font-size:6px;font-weight:600">
      <span style="width:28px;height:28px;border-radius:50%;background:#111;flex:none"></span>
      <span>VARRO V150 BLACK - HST-546<br>DRIVING - 46 MPH NEAR 123 SW<br>...SINCE 2:06 PM</span></div>
  </div>
</section>

<!-- Vehicle map -->
<section class="screen" style="left:351px;top:668px">
  <div class="abs map" role="img" aria-label="Street map around vehicle location" style="inset:0 0 auto 0;height:210px"></div>
  <div class="abs" style="left:92px;top:100px;width:62px;height:62px;border-radius:50%;background:rgba(60,80,140,.55)"></div>
  <div class="head abs" style="top:0;left:0;right:0"><span class="back"><svg class="i"><use href="#back"/></svg></span>Varro V150 Black – HST-546<br>Last update 20 seconds ago</div>
  <div class="abs" style="top:210px;left:0;right:0">
    <div class="card" style="margin:0 10px;padding:10px;display:flex;gap:10px;font-size:7px;transform:translateY(-10px)">
      <span style="width:18px;height:18px;border-radius:50%;background:var(--blue-dark);flex:none"></span>
      <span>Varro V150 Black – HST-546<br>Parked - At School<br>Since 2:06 pm</span><span style="margin-left:auto;font-weight:700">⋮</span></div>
    <div class="status" style="padding-top:0"><span><svg class="i st"><use href="#bolt"/></svg><br>FUEL</span><span><svg class="i st"><use href="#bolt"/></svg><br>BATTERY</span><span><svg class="i st"><use href="#car"/></svg><br>ENGINE</span><span><svg class="i st"><use href="#gear"/></svg><br>DEVICE</span></div>
    <div style="background:var(--blue);color:#fff;display:flex;justify-content:space-around;padding:6px 0;font-size:6px;font-weight:700;text-align:center"><span>●<br>INFO</span><span>●<br>CARE</span><span>●<br>NOTIFICATIONS</span></div>
    <div class="row" style="padding-top:10px"><span class="ico" style="width:24px;height:24px;flex:none"><svg class="i"><use href="#chart"/></svg></span><span><span class="t">Weekly Driver Report</span><br><span class="s">View driving details And see where to improve</span></span></div>
    <div class="row"><span class="ico" style="width:24px;height:24px;flex:none"><svg class="i"><use href="#pin"/></svg></span><span><span class="t">Get Directions</span><br><span class="s">4 mi from Varro 150 Black</span></span></div>
  </div>
</section>

<!-- Details -->
<section class="screen" style="left:649px;top:668px">
  <div class="head"><span class="back"><svg class="i"><use href="#back"/></svg></span>Varro V150 Black – HST-546<br>Last update 20 seconds ago</div>
  <div class="band">Details</div>
  <div style="padding:10px 14px 2px">
    <div class="field"><div class="k">Nickname</div><div class="v">Varro 150 Black</div></div>
    <div class="field"><div class="k">License plate</div><div class="v">HST-546</div></div>
    <div class="field"><div class="k">VIN</div><div class="v">234567890</div></div>
    <div class="field"><div class="k">Odometer</div><div class="v">109,758</div></div>
    <div class="field"><div class="k">Make</div><div class="v">Varro</div></div>
    <div class="field"><div class="k">Model</div><div class="v">V150 Black</div></div>
    <div class="field"><div class="k">Year</div><div class="v">2020</div></div>
    <div class="field"><div class="k">Car type</div><div class="v">SUV</div></div>
    <div class="field"><div class="k">IMEI</div><div class="v">01234567890</div></div>
  </div>
  <div class="band">Renewals</div>
  <div style="padding:10px 14px">
    <div class="field"><div class="k">Oil</div><div class="v">45,345 miles</div></div>
    <div class="field"><div class="k">Tyres</div><div class="v">65,984 miles</div></div>
    <div class="field"><div class="k">Leasing</div></div>
  </div>
</section>

<!-- Insurance -->
<section class="screen" style="left:922px;top:668px">
  <div class="head"><span class="back"><svg class="i"><use href="#back"/></svg></span>Varro V150 Black – HST-546<br>Last update 20 seconds ago</div>
  <div style="padding:24px 10px 6px" class="field"><div class="k">Maintenance</div><div class="v">48,345 miles</div></div>
  <div class="band">Insurance</div>
  <div style="padding:10px 10px">
    <div class="field"><div class="k">Company</div><div class="v">Brightway Mutual</div></div>
    <div class="field"><div class="k">Policy expiration dates</div><div class="v">February 15, 2024</div></div>
    <div class="field"><div class="k">Policy number</div><div class="v">234567890</div></div>
    <div class="field"><div class="k">Agent name</div><div class="v">Sam Ortell</div></div>
    <div class="field"><div class="k">Contact number</div><div class="v">3055550188</div></div>
  </div>
</section>

<!-- ================= ROW 3 ================= -->

<!-- Renewals alert -->
<section class="screen" style="left:61px;top:1198px">
  <div role="img" aria-label="Driver at the wheel background photo" style="height:98px;background:linear-gradient(160deg,#2b7fc6,#0f5ea8)"></div>
  <div class="abs brand" style="top:26px;left:0;right:0;justify-content:center;color:#fff;font-size:20px"><span class="dot"></span>qTrovel</div>
  <div style="padding:22px 18px 14px;font-weight:700;font-size:8px">VARRO V150 BLACK – HST-546<br>LAST UPDATE 20 SECONDS AGO</div>
  <div style="display:flex;gap:12px;padding:0 18px">
    <span class="ico" style="width:40px;height:40px;flex:none"><svg class="i"><use href="#pin"/></svg></span>
    <span style="font-size:8px"><b style="font-size:9.5px">RENEWALS / TYRES</b><br>Next Tyre Change<br><span class="blue" style="font-size:7px">65,984 Miles</span></span>
  </div>
</section>

<!-- Earlier today -->
<section class="screen" style="left:351px;top:1198px">
  <div style="background:linear-gradient(90deg,#fff 55%,var(--blue) 55%);height:46px"></div>
  <div class="head abs" style="top:0;left:0;right:0;padding-top:10px"><span class="back pale"><svg class="i"><use href="#back"/></svg></span>Varro V150 Black – HST-546<br>Last update 20 seconds ago</div>
  <div class="card" style="margin:-6px 12px 0;padding:8px 10px;display:flex;gap:10px;font-size:7px">
    <span style="width:18px;height:18px;border-radius:50%;background:var(--blue-dark);flex:none"></span>
    <span>Varro V150 Black – HST-546<br>Parked - At School<br>Since 2:06 pm</span><span style="margin-left:auto;font-weight:700">⋮</span></div>
  <div class="status" style="padding-top:12px"><span><svg class="i st"><use href="#bolt"/></svg><br>FUEL</span><span><svg class="i st"><use href="#bolt"/></svg><br>BATTERY</span><span><svg class="i st"><use href="#car"/></svg><br>ENGINE</span><span><svg class="i st"><use href="#gear"/></svg><br>DEVICE</span></div>
  <div class="row"><span class="ico" style="width:24px;height:24px;flex:none"><svg class="i"><use href="#chart"/></svg></span><span><span class="t">Weekly Driver Report</span><br><span class="s">View driving details And see where to improve</span></span></div>
  <div class="row"><span class="ico" style="width:24px;height:24px;flex:none"><svg class="i"><use href="#pin"/></svg></span><span><span class="t">Get Directions</span><br><span class="s">4 mi from Varro 150 Black<br>Tap to view ETA</span></span></div>
  <div class="section">Earlier Today</div>
  <div class="row"><span class="ico" style="width:24px;height:24px;flex:none"><svg class="i"><use href="#pin"/></svg></span><span><span class="t">Calle Marisol Vega, Lunara</span><br><span class="s">7:56 am-8:02 am (6min)</span><br><span style="display:inline-block;background:var(--blue);color:#fff;border-radius:6px;padding:1px 7px;font-size:6.5px;margin-top:3px">Add To Places</span></span></div>
  <div class="row"><span class="ico on" style="width:24px;height:24px;flex:none"><svg class="i"><use href="#car"/></svg></span><span><span class="t">4 Mile Drive</span><br><span class="s">7:36 am-7:56 am (19 min)</span></span></div>
  <div class="map" role="img" aria-label="Route map of the drive" style="margin:6px 14px 0;height:70px;border-radius:6px;background:var(--map-green)"></div>
</section>

<!-- Trips -->
<section class="screen" style="left:649px;top:1198px">
  <div class="head" style="padding-bottom:6px"><span class="back pale"><svg class="i"><use href="#back"/></svg></span>Varro V150 Black – HST-546<br>Last update 20 seconds ago</div>
  <div class="stats"><span><b>51 MPH</b>Top speed</span><span><b>3</b>Events</span><span class="no"><b>NO</b>Crash<br>Detection</span></div>
  <div class="row" style="padding-top:14px"><span class="ico on" style="width:24px;height:24px;flex:none"><svg class="i"><use href="#home"/></svg></span><span><span class="t">At Home</span><br><span class="s">3:17 pm-7:36 am (16 hr 18 min)</span></span></div>
  <div class="section">Yesterday</div>
  <div class="row"><span class="ico on" style="width:24px;height:24px;flex:none"><svg class="i"><use href="#car"/></svg></span><span><span class="t">9 Mile Drive</span><br><span class="s">2:54 pm-3:17 pm (22 min)</span></span></div>
  <div role="img" aria-label="Route map of the drive" style="margin:6px 14px;height:82px;border-radius:6px;background:var(--map-green)"></div>
  <div class="stats"><span><b>56 MPH</b>Top speed</span><span><b>7</b>Events</span><span class="no"><b>NO</b>Crash<br>Detection</span></div>
  <div class="row" style="padding-top:12px"><span class="ico on" style="width:24px;height:24px;flex:none"><svg class="i"><use href="#user"/></svg></span><span><span class="t">At School</span><br><span class="s">9:07 am-2:54 pm (5 hr 47 min)</span></span></div>
  <div class="row"><span class="ico on" style="width:24px;height:24px;flex:none"><svg class="i"><use href="#car"/></svg></span><span><span class="t">9 Mile Drive</span><br><span class="s">7:46 am-8:02 am (16m...</span></span></div>
  <div role="img" aria-label="Route map" style="margin:6px 14px 0;height:30px;border-radius:6px;background:var(--map-green)"></div>
</section>

<!-- Sunday -->
<section class="screen" style="left:922px;top:1198px">
  <div class="head" style="padding-bottom:6px"><span class="back pale"><svg class="i"><use href="#back"/></svg></span>Varro V150 Black – HST-546<br>Last update 20 seconds ago</div>
  <div class="stats"><span><b>51 MPH</b>Top speed</span><span><b>3</b>Events</span><span class="no"><b>NO</b>Crash<br>Detection</span></div>
  <div class="section" style="padding-top:14px">Sunday</div>
  <div class="row"><span class="ico on" style="width:24px;height:24px;flex:none"><svg class="i"><use href="#car"/></svg></span><span><span class="t">14 Mile Drive</span><br><span class="s">1:25 pm-2:09 pm (43 min)</span></span></div>
  <div role="img" aria-label="Route map of the drive" style="margin:6px 14px;height:82px;border-radius:6px;background:var(--map-green)"></div>
  <div class="stats"><span><b>49 MPH</b>Top speed</span><span><b>10</b>Events</span><span class="no"><b>NO</b>Crash<br>Detection</span></div>
  <div class="blue bold" style="text-align:right;padding:24px 22px 0;text-decoration:underline">CLICK FOR PAST DATA</div>
</section>

<!-- ================= ROW 4 ================= -->

<!-- Drive detail -->
<section class="screen" style="left:61px;top:1715px;background:#f4f6f8">
  <div role="img" aria-label="Route map of a 4-mile drive" style="height:190px;background:var(--map-green)"></div>
  <div class="abs" style="top:14px;left:10px;display:flex;gap:6px;font-size:8px;font-weight:700"><span class="back"><svg class="i"><use href="#back"/></svg></span><span>4-MILE DRIVE<br><span style="font-weight:500">7:46 AM – 8:02 AM (16 MIN)</span></span></div>
  <div class="card" style="margin:-10px 10px 0;padding:10px;font-size:6.5px;position:relative">7:57 am – 212 Elm Row, Brookhaven<br>Speed: 3.5 mph - Speed<br>Limit: 55 mph
    <div style="height:2px;background:var(--blue);margin:12px 0 2px;position:relative"><span class="abs" style="left:30px;top:-4px;width:10px;height:10px;border-radius:50%;background:var(--green)"></span></div></div>
  <div class="section" style="font-size:7.5px">Varro V150 Black's Drive Details</div>
  <div class="card" style="margin:4px 40px 6px 14px;display:flex;font-size:5.5px;padding:6px 8px"><span style="flex:1" class="blue">IDLE<br><b style="color:var(--ink);font-size:9px">3</b> MINUTES</span><span style="flex:1" class="blue">MAX SPEED<br><b style="color:var(--ink);font-size:9px">51.5</b> MPH</span></div>
  <div class="card" style="margin:0 40px 6px 14px;display:flex;font-size:5.5px;padding:6px 8px"><span style="flex:1" class="blue">FUEL CONSUMPTION<br><b style="color:var(--ink);font-size:9px">3.2</b> GALLONS</span><span style="flex:1" class="blue">FUEL ECONOMY<br><b style="color:var(--ink);font-size:9px">19.3</b> MPG</span></div>
  <div class="section" style="font-size:7.5px;padding-bottom:6px">Habits</div>
  <div class="habits">
    <span class="habit" style="background:var(--h-green)"><b>2</b>RAPID ACCEL</span><span class="habit" style="background:var(--h-blue)"><b>1</b>SHARP TURN</span><span class="habit" style="background:var(--h-gold)"><b>–</b>RAPID ACCEL</span><span class="habit" style="background:var(--h-red)"><b>2</b>SHARP TURN</span><span class="habit" style="background:var(--h-purple)"><b>–</b>SHARP TURN</span>
  </div>
</section>

<!-- Report summary -->
<section class="screen" style="left:351px;top:1715px">
  <div class="tabs"><span class="ico"><svg class="i"><use href="#car"/></svg></span><span class="ico"><svg class="i"><use href="#gear"/></svg></span><span class="ico on"><svg class="i"><use href="#chart"/></svg></span></div>
  <div class="chips"><span class="chip"><span class="c"></span>All</span><span class="chip"><span class="c b"></span>Varro V150 Black</span><span class="chip"><span class="c w"></span>Calder White</span><span class="chip"><span class="c"></span>Tobin's Truck</span><span class="chip"><span class="c"></span>Arlo's SUV</span></div>
  <div style="display:flex;justify-content:space-between;padding:20px 14px 14px;font-size:8px;font-weight:700"><span>‹</span>JUL 10 – JUL 16<span>›</span></div>
  <div class="card" style="margin:0 20px;display:flex;padding:8px 12px;font-size:5.5px;color:var(--muted)"><span style="flex:1"><b style="display:block;color:var(--ink);font-size:9px">138</b>Total Miles</span><span style="flex:1"><b style="display:block;color:var(--ink);font-size:9px">63 mph</b>Top Speed</span></div>
  <div style="margin:8px 20px 0;display:flex;padding:10px 12px;font-size:5.5px;background:var(--blue);color:#fff;border-radius:4px"><span style="flex:1"><b style="display:block;font-size:9px">16</b>Total Drives</span><span style="flex:1"><b style="display:block;font-size:9px">85</b>Driver's Score</span></div>
  <div style="padding-top:26px">
    <div class="list-item"><svg class="i blue"><use href="#gauge"/></svg>Excessive Speed<span class="n">3 <span class="blue">›</span></span></div>
    <div class="list-item"><svg class="i blue"><use href="#car"/></svg>Hard Braking<span class="n">8 <span class="blue">›</span></span></div>
    <div class="list-item"><svg class="i blue"><use href="#car"/></svg>Collison Detection<span class="n">0 <span class="blue">›</span></span></div>
    <div class="list-item"><svg class="i blue"><use href="#gauge"/></svg>Rapid Aceleration<span class="n">4 <span class="blue">›</span></span></div>
    <div class="list-item"><svg class="i blue"><use href="#back"/></svg>Sharp Turn<span class="n">6 <span class="blue">›</span></span></div>
  </div>
</section>

<!-- Excessive speed -->
<section class="screen" style="left:649px;top:1715px">
  <div class="tabs"><span class="ico"><svg class="i"><use href="#car"/></svg></span><span class="ico"><svg class="i"><use href="#gear"/></svg></span><span class="ico on"><svg class="i"><use href="#chart"/></svg></span></div>
  <div class="chips"><span class="chip"><span class="c"></span>All</span><span class="chip"><span class="c b"></span>Varro V150 Black</span><span class="chip"><span class="c w"></span>Calder White</span><span class="chip"><span class="c"></span>Tobin's Truck</span><span class="chip"><span class="c"></span>Arlo's SUV</span></div>
  <div style="display:flex;justify-content:space-between;padding:20px 14px 14px;font-size:8px;font-weight:700"><span>‹</span>JUL 10 – JUL 16<span>›</span></div>
  <div class="list-item" style="height:22px"><span class="blue">‹</span><svg class="i blue"><use href="#gauge"/></svg>Excessive Speed<span class="n">3</span></div>
  <div style="padding:10px 14px 0;font-size:6.5px"><b>WHAT IS "EXCESSIVE SPEED"?</b><br><span style="font-size:5.5px">Captures when a vehicle exceeds the speed limit.</span></div>
  <svg class="abs" style="left:12px;top:278px" width="156" height="72" viewBox="0 0 156 72" role="img" aria-label="Weekly excessive speed events chart">
    <rect width="156" height="72" rx="4" fill="#e9ecfb"/>
    <g fill="#7a8fe0"><circle cx="40" cy="56" r="2.5"/><circle cx="58" cy="56" r="2.5"/><circle cx="76" cy="56" r="2.5"/></g>
    <g font-size="5" fill="#333" text-anchor="middle" font-family="Poppins,sans-serif"><text x="20" y="62">0</text><text x="40" y="62">1</text><text x="58" y="62">1</text><text x="76" y="62">1</text><text x="96" y="62">0</text><text x="116" y="62">0</text><text x="136" y="62">0</text>
    <text x="20" y="68">Mon</text><text x="40" y="68">Tue</text><text x="58" y="68">Wed</text><text x="76" y="68">Thu</text><text x="96" y="68">Fri</text><text x="116" y="68">Sat</text><text x="136" y="68">Sun</text></g>
  </svg>
  <div class="abs" style="top:364px;left:0;right:0">
    <div class="section" style="padding-top:0">Thursday Jul 13</div>
    <div class="row"><span class="ico on" style="width:22px;height:22px;flex:none"><svg class="i"><use href="#car"/></svg></span><span><span class="t">16 Mile Drive</span><br><span class="s">2:50 pm-3:09 pm</span></span></div>
    <div class="section" style="padding-top:2px">Wednesday Jul 12</div>
    <div class="row"><span class="ico on" style="width:22px;height:22px;flex:none"><svg class="i"><use href="#car"/></svg></span><span><span class="t">16 Mile Drive</span><br><span class="s">3:58 pm-4:51 pm</span></span></div>
  </div>
</section>

<!-- Driver score -->
<section class="screen" style="left:922px;top:1715px">
  <div class="tabs"><span class="ico"><svg class="i"><use href="#car"/></svg></span><span class="ico"><svg class="i"><use href="#gear"/></svg></span><span class="ico on"><svg class="i"><use href="#chart"/></svg></span></div>
  <div class="card" style="margin:12px 10px 0;padding:10px;display:flex;gap:10px;font-size:7px">
    <span style="width:18px;height:18px;border-radius:50%;background:var(--blue-dark);flex:none"></span>
    <span>Varro V150 Black – HST-546 Parked<br>At School Since 2:06 pm</span></div>
  <div class="blue bold" style="padding:18px 22px 0;font-size:11px">Driver's Score</div>
  <div style="display:flex;align-items:center;padding:4px 14px 0 22px">
    <span class="bold" style="font-size:26px">85</span>
    <svg width="110" height="64" viewBox="0 0 110 64" style="margin-left:auto" role="img" aria-label="Driver score gauge at 85">
      <path d="M15 56 A40 40 0 0 1 35 22" stroke="#e02a2a" stroke-width="9" fill="none"/>
      <path d="M35 22 A40 40 0 0 1 55 16" stroke="#f28b1e" stroke-width="9" fill="none"/>
      <path d="M55 16 A40 40 0 0 1 78 23" stroke="#f5c71a" stroke-width="9" fill="none"/>
      <path d="M78 23 A40 40 0 0 1 95 56" stroke="#3aa845" stroke-width="9" fill="none"/>
      <circle cx="55" cy="56" r="8" fill="none" stroke="#888" stroke-width="2"/><path d="M55 56 L82 36" stroke="#888" stroke-width="2"/>
      <g font-size="4" fill="#333" font-family="Poppins,sans-serif"><text x="4" y="63">Risky Driver</text><text x="88" y="63">Ideal Driver</text></g>
    </svg>
  </div>
  <div style="padding:20px 22px 4px;font-size:10px;font-weight:700">What is the Driver's Score?</div>
  <div style="padding:0 22px;font-size:5.5px">The Driver's Score is a carefully checked measure shown to reliably reflect safe habits and road risk factors for each of your drivers.</div>
  <div style="display:flex;justify-content:space-around;padding:16px 18px 0;text-align:center;font-size:4.5px">
    <span><span style="display:block;width:30px;height:30px;border-radius:50%;border:2.5px solid #f28b1e;line-height:25px;font-size:11px">85</span>Acceleration</span>
    <span><span style="display:block;width:30px;height:30px;border-radius:50%;border:2.5px solid #e02a2a;line-height:25px;font-size:11px">62</span>Braking</span>
    <span><span style="display:block;width:30px;height:30px;border-radius:50%;border:2.5px solid #3aa845;line-height:25px;font-size:11px">58</span>Cornering</span>
    <span><span style="display:block;width:30px;height:30px;border-radius:50%;border:2.5px solid var(--h-purple);line-height:25px;font-size:11px">98</span>Speed</span>
  </div>
  <div class="section" style="font-size:7.5px;padding-bottom:6px">Habits</div>
  <div class="habits">
    <span class="habit" style="background:var(--h-green)"><b>2</b>RAPID ACCEL</span><span class="habit" style="background:var(--h-blue)"><b>1</b>SHARP TURN</span><span class="habit" style="background:var(--h-gold)"><b>–</b>RAPID ACCEL</span><span class="habit" style="background:var(--h-red)"><b>2</b>SHARP TURN</span><span class="habit" style="background:var(--h-purple)"><b>–</b>SHARP TURN</span>
  </div>
</section>

<!-- ================= ROW 5 ================= -->

<!-- Vehicle profile -->
<section class="screen" style="left:61px;top:2232px;background:#f4f6f8">
  <div role="img" aria-label="Blue-tinted car photo banner" style="height:110px;background:linear-gradient(160deg,#2b7fc6,#0f5ea8)"></div>
  <div class="abs" role="img" aria-label="Vehicle photo" style="left:82px;top:70px;width:56px;height:56px;border-radius:50%;background:linear-gradient(#f3d35a,#c99a22);border:3px solid #fff"></div>
  <div style="text-align:center;padding-top:28px;font-size:12px;font-weight:600">WRENNA'S CAR</div>
  <div class="blue" style="text-align:center;font-size:7px">Share Vehicle</div>
  <div style="display:flex;justify-content:center;gap:6px;padding:12px 0;font-size:6px;font-weight:700">
    <span style="background:var(--blue);color:#fff;padding:2px 10px">DETAILS</span><span style="background:#fff;padding:2px 8px">RENEWALS</span><span style="background:#fff;padding:2px 8px">INSURANCE</span></div>
  <div class="card" style="margin:4px 10px;padding:12px 12px;font-size:7px">
    <div style="display:flex;font-weight:700;font-size:8px;padding-bottom:8px">VEHICLE DATAILS<span class="blue" style="margin-left:auto;font-size:7px">Edit</span></div>
    <div style="display:grid;grid-template-columns:92px 1fr;row-gap:6.5px;padding-left:4px">
      <span>Nickname</span><span>Wrenna's Car</span><span>License Plate</span><span></span><span>Odometer</span><span>119145 miles</span><span>VIN</span><span></span><span>Make</span><span>HOLLEN</span><span>Model</span><span>Pipit</span><span>Year</span><span>2008</span><span>Body Style</span><span>Convertible/Cabriolet</span><span>Engine</span><span>2.5L</span><span>IMEI</span><span></span>
    </div>
  </div>
</section>

<!-- Notifications -->
<section class="screen" style="left:351px;top:2232px">
  <div style="display:flex;align-items:center;gap:8px;padding:14px 10px 6px;font-size:9px;font-weight:600"><svg class="i" style="width:10px"><use href="#back"/></svg>Wrenna's Car Notifications<span class="blue" style="margin-left:auto;font-size:7px">EDIT</span></div>
  <div style="display:flex;justify-content:center;gap:10px;font-size:6px;font-weight:700;padding-bottom:6px"><span>Drive</span><span style="background:var(--blue);color:#fff;padding:1px 10px;border-radius:3px">Vehicle</span><span>Care</span></div>
  <div style="background:linear-gradient(#fff,#eef0f3)">
    <div class="row" style="padding:8px 14px;height:58px"><span class="ico on" style="width:30px;height:30px;flex:none"><svg class="i"><use href="#car"/></svg></span><span><span class="t" style="font-size:7px">Plimsy was reconnected on Wrenna's car.</span><br><span style="font-size:5px">Plimsy was offline for 1 minute starting July 1, 2023 3:52 PM</span></span></div>
  </div>
  <div style="background:linear-gradient(#fff,#eef0f3)">
    <div class="row" style="padding:8px 14px;height:58px"><span class="ico on" style="width:30px;height:30px;flex:none"><svg class="i"><use href="#car"/></svg></span><span><span class="t" style="font-size:7px">Plimsy was reconnected on Wrenna's car.</span><br><span style="font-size:5px">Plimsy was offline for 1 minute starting July 1, 2023 3:52 PM</span></span></div>
  </div>
  <div style="background:linear-gradient(#fff,#eef0f3)">
    <div class="row" style="padding:8px 14px;height:58px"><span class="ico on" style="width:30px;height:30px;flex:none"><svg class="i"><use href="#car"/></svg></span><span><span class="t" style="font-size:7px">Plimsy was reconnected on Wrenna's car.</span><br><span style="font-size:5px">Plimsy was offline for 1 minute starting July 1, 2023 3:52 PM</span></span></div>
  </div>
  <div style="background:linear-gradient(#fff,#eef0f3)"><div class="row" style="padding:8px 14px;height:53px"><span class="ico on" style="width:30px;height:30px;flex:none"><svg class="i"><use href="#bolt"/></svg></span><span><span class="t" style="font-size:7px">The battery level for Wrenna's car is low.</span><br><span style="font-size:5px">The Battery Level For Wrenna's Car is low</span></span></div></div>
  <div style="background:linear-gradient(#fff,#eef0f3)"><div class="row" style="padding:8px 14px;height:53px"><span class="ico on" style="width:30px;height:30px;flex:none"><svg class="i"><use href="#bolt"/></svg></span><span><span class="t" style="font-size:7px">The battery level for Wrenna's car is low.</span><br><span style="font-size:5px">The Battery Level For Wrenna's Car is low</span></span></div></div>
  <div style="background:linear-gradient(#fff,#eef0f3)"><div class="row" style="padding:8px 14px;height:53px"><span class="ico on" style="width:30px;height:30px;flex:none"><svg class="i"><use href="#bolt"/></svg></span><span><span class="t" style="font-size:7px">The battery level for Wrenna's car is low.</span><br><span style="font-size:5px">The Battery Level For Wrenna's Car is low</span></span></div></div>
  <div style="background:linear-gradient(#fff,#eef0f3)"><div class="row" style="padding:8px 14px;height:53px"><span class="ico on" style="width:30px;height:30px;flex:none"><svg class="i"><use href="#bolt"/></svg></span><span><span class="t" style="font-size:7px">The battery level for Wrenna's car is low.</span><br><span style="font-size:5px">The Battery Level For Wrenna's Car is low</span></span></div></div>
  <div class="abs blue" style="left:14px;right:14px;bottom:6px;display:flex;justify-content:space-between;font-size:7px;font-weight:600"><span>Clear All</span><span>Settings</span></div>
</section>

</body>
</html>
```